Updated DJ business Card showing other businesses

DJ Kestro offers professional mobile dj services including DJ. MC. Karaoke.
Silent Disco (will attach logo)
I also offer a 360 Photo Booth.

Contact info:
(555) 013-4472
marcus.tellgren@lumomail.net
Social Media @DJKestroNWX

```html
<!DOCTYPE html>
<html lang="en">
<head>
<meta charset="utf-8">
<title>DJ Kestro — Business Cards</title>
<link href="https://fonts.googleapis.com/css2?family=Montserrat:wght@500;800&display=swap" rel="stylesheet">
<style>
  :root {
    --backdrop: #2e2e2e;
    --card: #ffffff;
    --ink: #141414;
    --accent: #d41f45;
  }
  * { box-sizing: border-box; margin: 0; padding: 0; }
  html, body {
    width: 1200px;
    height: 689px;
    overflow: hidden;
    background: var(--backdrop);
    font-family: "Montserrat", Arial, sans-serif;
  }
  .canvas {
    position: relative;
    width: 1200px;
    height: 689px;
    display: flex;
    align-items: center;
    justify-content: center;
    gap: 40px;
  }
  .card {
    width: 540px;
    height: 309px;
    background: var(--card);
    border-radius: 20px;
    position: relative;
    overflow: hidden;
  }
  /* Front: service mark */
  .card-front {
    display: flex;
    align-items: center;
    justify-content: center;
  }
  .service-mark {
    display: flex;
    align-items: center;
    gap: 16px;
  }
  .service-mark-dot {
    width: 54px;
    height: 54px;
    border-radius: 50%;
    background: var(--ink);
  }
  .service-mark-name {
    font-weight: 800;
    font-size: 46px;
    letter-spacing: 1px;
    color: var(--ink);
    text-transform: uppercase;
    line-height: 1;
  }
  /* Back: brand + contact */
  .card-back {
    display: flex;
    align-items: center;
    justify-content: center;
    padding: 0 28px;
  }
  .brand-name {
    font-weight: 800;
    font-size: 34px;
    color: var(--accent);
    letter-spacing: 0.3px;
    white-space: nowrap;
    line-height: 1;
  }
  .divider {
    width: 2px;
    height: 80px;
    background: var(--accent);
    margin: 0 14px 0 16px;
    flex-shrink: 0;
  }
  .contact-list {
    list-style: none;
    display: flex;
    flex-direction: column;
    gap: 7px;
    min-width: 0;
  }
  .contact-item {
    display: flex;
    align-items: center;
    gap: 6px;
    font-weight: 500;
    font-size: 12px;
    color: var(--ink);
    white-space: nowrap;
  }
  .contact-icon {
    width: 12px;
    height: 12px;
    flex-shrink: 0;
    fill: var(--accent);
  }
  .social-square {
    width: 10px;
    height: 10px;
    background: var(--accent);
    flex-shrink: 0;
    margin: 0 1px;
  }
</style>
</head>
<body>
  <main class="canvas">
    <section class="card card-front" aria-label="Card front">
      <div class="service-mark">
        <span class="service-mark-dot" aria-hidden="true"></span>
        <span class="service-mark-name">Silent Disco</span>
      </div>
    </section>

    <section class="card card-back" aria-label="Card back">
      <h1 class="brand-name">DJ KESTRO</h1>
      <span class="divider" aria-hidden="true"></span>
      <ul class="contact-list">
        <li class="contact-item">
          <svg class="contact-icon" viewBox="0 0 24 24" aria-hidden="true">
            <path d="M6.6 10.8a15.1 15.1 0 0 0 6.6 6.6l2.2-2.2a1 1 0 0 1 1-.25 11.4 11.4 0 0 0 3.6.57 1 1 0 0 1 1 1V20a1 1 0 0 1-1 1A17 17 0 0 1 3 4a1 1 0 0 1 1-1h3.5a1 1 0 0 1 1 1c0 1.25.2 2.45.57 3.57a1 1 0 0 1-.25 1z"/>
          </svg>
          (555) 013-4472
        </li>
        <li class="contact-item">
          <svg class="contact-icon" viewBox="0 0 24 24" aria-hidden="true">
            <path d="M2 5h20v14H2z M2 5l10 8 10-8" fill="none" stroke="#d41f45" stroke-width="2.4" stroke-linejoin="round"/>
          </svg>
          marcus.tellgren@lumomail.net
        </li>
        <li class="contact-item">
          <span class="social-square" aria-hidden="true"></span>
          @DJKestroNWX
        </li>
      </ul>
    </section>
  </main>
</body>
</html>
```